Flyer-Design für bildenden Künstler
Die einzige Designerin, die es wirklich verstanden hat, mein ausführliches briefing in einem wunderschönen, eleganten und absolut einzigartigen Design umzusetzen. Die Zusammenarbeit war klasse, sie ist auf jede meiner Wünsche eingegangen und hat sie mit großer Geduld und Professionalität umgesetzt. Das hätte nicht besser laufen können. Bin begeistert, von ihrem künstlerischen Anspruch, dem feinen Sinn für Ästhetik und ihrer großen Kreativität.
Zielgruppe
Ich bin bildender Künstler, benötige einen außergewöhnlichen, sehr ästhetischen, einzigartigen, als Eyecatcher fungierenden, meine Kunst und Identität repräsentierenden Flyer zum Auslegen, um neue KundInnen zu gewinnen.
Aufgabenstellung
Er soll wenig Text beinhalten (ein Zitat, Anschrift und Kontaktmöglichkeiten, ein kleines statement zu meiner Kunstphilosophie), und Bilder meiner Kunst zeigen. Raum ist mir wichtig, genug Leerräume, damit ein in Szene gesetztes Zitat oder Foto meiner Kunstwerke gut wirken kann. Es soll Lust darauf machen, Anreiz bieten und Interesse wecken, auf meine homepage zu gehen. Die Einzigartigkeit meiner Kunst soll deutlich werden.
Die hochgelandenen Fotos zeigen meine Kunstwerke. Sie können als Hintergrundbild fungieren und dementsprechend auch die ganze Seite ausfüllen, sie können zugeschnitten werden und/oder mit Text überlagert sein. Manche Fotos (zum Beispiel die Kunstwerke mit Rahmen) eignen sich dagegen, sie auf einer ganzen Seite zu zeigen, ohne einen Text dazu. So eine Seite würde ich jedenfalls gerne dabei haben, wo ein Kunstwerk für sich alleine auf einer ganzen Seite dargestellt wird. 1O4A2598 oder 1O4A6076a bieten sich dafür an (diese und alle anderen Fotos sind zum Teil komprimiert und zugeschnitten; falls gewünscht bzw. die Qualität nicht gut ist, kann ich das Originalfoto senden, das unkomprimiert und nicht zugeschnitten ist. Auch kann die Helligkeit oder die Farbqualität verbessert werden, falls notwendig). Nicht alle Kunstbilder müssen verwendet werden.
Ich bin offen für jedes Flyerformat, tendiere zu einem ein 2 oder 3-seitigen Falzflyer hochkant oder im Querformat. Bin aber offen für Ideen und Vorschläge.
Die Texte unter der Datei 'Texte, Adresse, Zitate' enthalten einen kleinen Text, der verwendet werden soll. Unter 'Text für die Titelseite' ist ein Vorschlag für die Titelseite zu finden. Die Adresse muss vollständig erscheinen, und unter 'Zitate' sind mehrere meiner Zitate - auch davon soll eines verwendet werden.
BITTE AUSSCHLIEßLICH DIE FOTOS UND TEXTE VERWENDEN, DIE ICH HOCHGELADEN HABE, UND NICHTS VON MEINEN HOMEPAGES NEHMEN. DANKE!

```html
<!DOCTYPE html>
<html lang="de">
<head>
<meta charset="utf-8">
<title>Wendler Art – Falzflyer Transformationen</title>
<link rel="stylesheet" href="https://fonts.googleapis.com/css2?family=Montserrat:wght@400;500;700;800&display=swap">
<style>
  :root {
    --backdrop: #e9edf0;
    --steel-blue: #6f8fa3;
    --steel-blue-dark: #5a7a8e;
    --title-blue: #55829c;
    --paper: #f7f7f7;
    --paper-grey: #d6d6d6;
    --paper-grey-light: #ececec;
    --ink: #4a4f55;
    --art-teal: #2f93b3;
    --art-deep: #1f6f8a;
    --frame: #cfd2d4;
    --logo-sand: #b9a588;
  }
  * { box-sizing: border-box; margin: 0; padding: 0; }
  html, body {
    width: 1200px; height: 900px; overflow: hidden;
    background: var(--backdrop);
    font-family: "Montserrat", sans-serif;
    color: var(--ink);
  }
  .stage {
    width: 1200px; height: 900px;
    display: flex; align-items: center; justify-content: center; gap: 24px;
  }
  .sheet {
    width: 570px; height: 403px;
    display: flex;
    box-shadow: 0 10px 30px rgba(40, 60, 75, 0.18);
  }
  .panel {
    position: relative;
    width: 190px; height: 100%;
    overflow: hidden;
  }

  /* Outside */
  .panel--quote {
    background: var(--steel-blue);
    color: #fff;
    display: flex; flex-direction: column; align-items: center; justify-content: center;
    padding: 0 18px 40px;
    text-align: center;
  }
  .quote-mark {
    font-weight: 800; font-size: 46px; line-height: 0.6; height: 26px;
    margin-bottom: 18px;
  }
  .quote-text {
    font-weight: 700; font-size: 10.5px; line-height: 1.75;
  }
  .panel--contact {
    background: linear-gradient(90deg, #ffffff 0%, #f0f0f0 100%);
    display: flex; flex-direction: column; justify-content: flex-end; align-items: center;
    padding-bottom: 42px;
    text-align: center;
    font-size: 7.5px; line-height: 1.45;
    color: var(--steel-blue-dark);
  }
  .contact-name { font-weight: 700; }
  .contact-block + .contact-block { margin-top: 12px; }
  .contact-web { font-weight: 700; }
  .panel--cover {
    background: linear-gradient(90deg, #d9d9d9 0%, #c9c9c9 100%);
    display: flex; flex-direction: column; align-items: center;
    padding-top: 30px;
  }
  .bottom-band {
    position: absolute; left: 0; right: 0; bottom: 0; height: 16px;
    background: var(--steel-blue);
  }
  .panel--cover .bottom-band { background: var(--steel-blue-dark); }

  .title {
    text-align: center; color: var(--title-blue);
    font-weight: 700; font-size: 19px; line-height: 1.12;
  }
  .subtitle {
    text-align: center; color: var(--title-blue);
    font-weight: 700; font-size: 11px; margin-top: 4px;
  }
  .rule {
    width: 20px; height: 3px; background: var(--steel-blue-dark);
    margin: 12px auto 0;
  }
  .art-circle { width: 126px; height: 126px; margin-top: 30px; }
  .wordmark {
    display: flex; align-items: center; gap: 5px;
    font-weight: 500; font-size: 13px; color: var(--ink);
    letter-spacing: 0.02em;
  }
  .wordmark-square { width: 7px; height: 7px; background: var(--logo-sand); }
  .panel--cover .wordmark { position: absolute; bottom: 42px; }

  /* Inside */
  .panel--philosophy {
    background: linear-gradient(90deg, #cfcfcf 0%, #e6e6e6 100%);
    padding: 50px 18px 0 28px;
  }
  .section-title {
    color: var(--title-blue); font-weight: 800; font-size: 17px; line-height: 1.3;
  }
  .panel--philosophy .rule { margin: 14px 0 0; }
  .philosophy-text {
    margin-top: 24px; font-size: 8.3px; line-height: 1.55; color: var(--steel-blue-dark);
  }
  .panel--philosophy .wordmark { position: absolute; left: 84px; bottom: 24px; }
  .spread {
    position: relative; width: 380px; height: 100%;
    background: linear-gradient(90deg, #efefef 0%, #fafafa 48%, #e9e9e9 50%, #fbfbfb 52%, #ffffff 100%);
    display: flex; flex-direction: column; justify-content: space-between;
    padding: 36px 18px 38px 20px;
  }
  .artwork-frame {
    height: 132px;
    border: 4px solid var(--frame);
    background: #3b4045;
    padding: 4px;
  }
  .artwork-frame svg { display: block; width: 100%; height: 100%; }
</style>
</head>
<body>
<main class="stage">

  <section class="sheet sheet--outside" aria-label="Flyer Außenseite">
    <div class="panel panel--quote">
      <div class="quote-mark" aria-hidden="true">&ldquo;</div>
      <p class="quote-text">Kunst unterstreicht Deinen guten Geschmack. Es zeugt davon, dass Du Weitblick besitzt. Und offen für neue Erfahrungen bist.</p>
    </div>

    <div class="panel panel--contact">
      <div class="contact-block">
        <p class="contact-name">Tobias Wendler</p>
        <p>Lindenhofweg 12</p>
        <p>79098 Freiburg</p>
      </div>
      <div class="contact-block">
        <p>(+49) 0761 555 0142</p>
        <p>wendler-art@example.de</p>
      </div>
      <div class="contact-block">
        <p class="contact-web">www.wendler-art.example</p>
      </div>
      <div class="bottom-band"></div>
    </div>

    <div class="panel panel--cover">
      <h1 class="title">Tobias<br>Wendler Art</h1>
      <p class="subtitle">Transformationen</p>
      <div class="rule"></div>
      <svg class="art-circle" viewBox="0 0 100 100" role="img" aria-label="Kreisausschnitt eines Kunstwerks aus blau gefärbten, porösen Steinen">
        <defs>
          <radialGradient id="circleTone" cx="45%" cy="40%" r="65%">
            <stop offset="0%" stop-color="#3aa3c2"/>
            <stop offset="100%" stop-color="#1d6680"/>
          </radialGradient>
        </defs>
        <circle cx="50" cy="50" r="50" fill="url(#circleTone)"/>
      </svg>
      <div class="wordmark"><span class="wordmark-square"></span>Wendler Art</div>
      <div class="bottom-band"></div>
    </div>
  </section>

  <section class="sheet sheet--inside" aria-label="Flyer Innenseite">
    <div class="panel panel--philosophy">
      <h2 class="section-title">The<br>Philosophy</h2>
      <div class="rule"></div>
      <p class="philosophy-text">Seit jeher fasziniert mich die Transformation eines Zustandes in einen anderen. Das ganze Leben ist eine fortwährende Veränderung, nichts bleibt, wie es ist. Ich setze mich damit auseinander und gebe Material und Vergangenem eine neue Sinnhaftigkeit.</p>
      <div class="wordmark"><span class="wordmark-square"></span>Wendler Art</div>
    </div>

    <div class="spread">
      <div class="artwork-frame">
        <svg viewBox="0 0 100 40" preserveAspectRatio="none" role="img" aria-label="Gerahmtes Kunstwerk aus blau gefärbten, porösen Steinen, Querformat">
          <defs>
            <linearGradient id="artToneA" x1="0" y1="0" x2="1" y2="1">
              <stop offset="0%" stop-color="#38a0c0"/>
              <stop offset="100%" stop-color="#23809f"/>
            </linearGradient>
          </defs>
          <rect width="100" height="40" fill="url(#artToneA)"/>
        </svg>
      </div>
      <div class="artwork-frame">
        <svg viewBox="0 0 100 40" preserveAspectRatio="none" role="img" aria-label="Zweites gerahmtes Kunstwerk aus blau gefärbten, porösen Steinen, Querformat">
          <defs>
            <linearGradient id="artToneB" x1="0" y1="1" x2="1" y2="0">
              <stop offset="0%" stop-color="#22809e"/>
              <stop offset="100%" stop-color="#3aa5c4"/>
            </linearGradient>
          </defs>
          <rect width="100" height="40" fill="url(#artToneB)"/>
        </svg>
      </div>
    </div>
  </section>

</main>
</body>
</html>
```